Business card for auto dealership

Looking for a clean modern design.
Would like attached logo incorporated

Industry/Entity Type

Car dealership

Contact Information for Business Card

Name, website, phone, cell, fax, email

```html
<!DOCTYPE html>
<html lang="en">
<head>
<meta charset="utf-8">
<title>Halvorsen Truck &amp; Auto Sales – Business Card</title>
<link rel="stylesheet" href="https://fonts.googleapis.com/css2?family=Oswald:wght@600;700&family=Anton&family=Open+Sans:wght@400&display=swap">
<style>
  :root {
    --navy: #343947;
    --navy-deep: #2c303c;
    --paper: #ffffff;
    --card-light: #f2f3f5;
    --ink: #151515;
    --muted: #8a8c90;
    --divider: #9da0a6;
  }
  * { box-sizing: border-box; margin: 0; padding: 0; }
  html, body {
    width: 1200px; height: 1200px; overflow: hidden;
    background: var(--paper);
  }
  .card {
    position: absolute;
    left: 221px;
    width: 771px; height: 466px;
    box-shadow: 0 14px 30px rgba(0,0,0,0.28);
    overflow: hidden;
  }
  .card--front { top: 60px; background: var(--paper); }
  .card--back  { top: 623px; background: var(--card-light); }

  .front-art { position: absolute; inset: 0; }

  .brand {
    position: absolute;
    text-align: center;
    font-family: "Oswald", sans-serif;
    font-weight: 700;
    line-height: 1;
  }
  .brand__name { display: block; font-size: 78px; letter-spacing: 1px; }
  .brand__tag  { display: block; font-size: 20px; letter-spacing: 1px; margin-top: 6px; }

  .card--front .brand { left: 0; width: 771px; top: 160px; color: var(--paper); }
  .card--back  .brand { left: 30px; width: 310px; top: 128px; color: var(--ink); }
  .card--back  .brand__name { font-size: 62px; }
  .card--back  .brand__tag  { font-size: 16px; }

  .divider {
    position: absolute;
    left: 371px; top: 49px;
    width: 2px; height: 334px;
    background: linear-gradient(to bottom, transparent, var(--divider) 15%, var(--divider) 85%, transparent);
  }

  .holder {
    position: absolute;
    left: 406px; top: 64px;
    font-family: "Anton", sans-serif;
    font-weight: 400;
    font-size: 48px;
    letter-spacing: 0.5px;
    color: var(--ink);
    line-height: 1;
    white-space: nowrap;
  }

  .contact-list { position: absolute; left: 419px; top: 0; list-style: none; }
  .contact {
    position: absolute;
    left: 0;
    display: flex; align-items: center;
    white-space: nowrap;
    font-family: "Oswald", sans-serif;
    font-weight: 700;
    font-size: 23px;
    color: var(--ink);
    transform: translateY(-50%);
  }
  .contact svg { width: 26px; height: 26px; margin-right: 12px; flex: none; }

  .address {
    position: absolute;
    left: 0; width: 771px; top: 436px;
    text-align: center;
    font-family: "Open Sans", sans-serif;
    font-size: 15px;
    letter-spacing: 1.4px;
    color: var(--muted);
  }
</style>
</head>
<body>

<section class="card card--front">
  <svg class="front-art" viewBox="0 0 771 466" role="img" aria-label="Dark navy background with a faint photograph of a semi truck on the road">
    <path d="M0 0 H771 V282 C600 355 360 418 0 423 Z" fill="var(--navy)"/>
    <path d="M771 302 C620 362 420 412 190 422 C440 416 640 372 771 320 Z" fill="var(--navy-deep)"/>
  </svg>
  <div class="brand">
    <span class="brand__name">Halvorsen</span>
    <span class="brand__tag">TRUCK &amp; AUTO SALES</span>
  </div>
</section>

<section class="card card--back">
  <div class="brand">
    <span class="brand__name">Halvorsen</span>
    <span class="brand__tag">TRUCK &amp; AUTO SALES</span>
  </div>

  <div class="divider"></div>

  <h1 class="holder">DANA WHITFIELD</h1>

  <ul class="contact-list">
    <li class="contact" style="top:155px">
      <svg viewBox="0 0 26 26" aria-hidden="true"><circle cx="13" cy="13" r="13" fill="var(--ink)"/><g fill="none" stroke="#fff" stroke-width="1.3"><circle cx="13" cy="13" r="7"/><ellipse cx="13" cy="13" rx="3" ry="7"/><path d="M6 13H20M7.5 9H18.5M7.5 17H18.5"/></g></svg>
      www.halvorsenauto.com
    </li>
    <li class="contact" style="top:205px">
      <svg viewBox="0 0 26 26" aria-hidden="true"><circle cx="13" cy="13" r="13" fill="var(--ink)"/><path d="M9 7 L11.5 10 L10 12 C11 14.5 12.5 16 15 17 L17 15.5 L20 18 L18 20 C12 20 7 14 7 8.5 Z" fill="#fff"/></svg>
      (716) 555-0142
    </li>
    <li class="contact" style="top:249px">
      <svg viewBox="0 0 26 26" aria-hidden="true"><circle cx="13" cy="13" r="13" fill="var(--ink)"/><rect x="9" y="6" width="8" height="14" rx="1.5" fill="none" stroke="#fff" stroke-width="1.4"/><circle cx="13" cy="17.5" r="0.9" fill="#fff"/></svg>
      (716) 555-0187
    </li>
    <li class="contact" style="top:299px">
      <svg viewBox="0 0 26 26" aria-hidden="true"><circle cx="13" cy="13" r="13" fill="var(--ink)"/><rect x="7" y="11" width="12" height="8" rx="1" fill="#fff"/><rect x="9" y="7" width="8" height="5" fill="none" stroke="#fff" stroke-width="1.3"/><rect x="10" y="14" width="6" height="1.2" fill="var(--ink)"/></svg>
      +1-716-555-0199
    </li>
    <li class="contact" style="top:346px">
      <svg viewBox="0 0 26 26" aria-hidden="true"><circle cx="13" cy="13" r="13" fill="var(--ink)"/><rect x="7" y="8.5" width="12" height="9" rx="1" fill="none" stroke="#fff" stroke-width="1.3"/><path d="M7.5 9 L13 14 L18.5 9" fill="none" stroke="#fff" stroke-width="1.3"/></svg>
      email@halvorsenauto.com
    </li>
  </ul>

  <p class="address">4820 Ridge Road, Millbrook, NY 14500, United States</p>
</section>

</body>
</html>
```